Do it yourself Karten und Hochzeitsdeko selbstgemacht
Zielgruppe
Wir sind ein Bastelgeschäft. Wir bieten Materialien zum selber machen von Karten, Tischkarten,Menükarten, Gästebüchern, Fotoalben an.
Alle Materialien zur Anlassgestaltung, auch Tischdeko und Kerzen.
Zielgruppe: Junge Leute auf einer Hochzeitsmesse
Aufgabenstellung
Ich benötige einen Flyer in A5 Format. Einige Fotoausschnitte und Text. Romantisch.
Fotos von angefertigten Karten und Deko sind vorhanden.
Logo vorhanden, soll mit rein und Öffnungszeiten mit Internet
Text: Do it Yourself Karten und Hochzeitsdeko selbst gemacht!
Zeiten etc. bitte www.falten-und-schmuecken.de

```html
<!DOCTYPE html>
<html lang="de">
<head>
<meta charset="utf-8">
<title>Do it yourself – Flyer</title>
<link href="https://fonts.googleapis.com/css2?family=Great+Vibes&family=Dancing+Script:wght@600&family=Didact+Gothic&display=swap" rel="stylesheet">
<style>
  :root {
    --teal: #4b979e;
    --teal-dark: #3f878e;
    --ink: #222222;
    --paper: #ffffff;
    --bg-top: #ececec;
    --bg-bottom: #6a6a6a;
    --grey-mark: #8c8c8c;
    --photo-light: #e9e9ee;
    --photo-mid: #c9ccd2;
  }
  * { margin: 0; padding: 0; box-sizing: border-box; }
  html, body { width: 1200px; height: 810px; overflow: hidden; }
  body {
    position: relative;
    background: linear-gradient(180deg, var(--bg-top) 0%, #d2d2d2 40%, var(--bg-bottom) 100%);
    font-family: "Didact Gothic", "Century Gothic", sans-serif;
    color: var(--ink);
  }
  .page {
    position: absolute;
    top: 25px;
    width: 535px;
    height: 761px;
    background: var(--paper);
    box-shadow: 0 2px 8px rgba(0,0,0,.25);
    overflow: hidden;
  }
  .page--front { left: 47px; }
  .page--back { left: 619px; }

  /* front */
  .header-band {
    position: absolute; left: 0; top: 0; width: 100%; height: 233px;
    background: var(--teal);
    box-shadow: 0 6px 8px -4px rgba(0,0,0,.35);
  }
  .shop-mark {
    position: absolute; display: flex; align-items: center; justify-content: center;
    border-radius: 50%; border: 2px solid #fff;
  }
  .shop-mark span {
    font-family: "Didact Gothic", sans-serif; color: #fff; font-size: 24px; letter-spacing: 1px;
  }
  .header-band .shop-mark {
    left: 33px; top: 32px; width: 150px; height: 150px; background: var(--grey-mark);
  }
  .headline {
    position: absolute; left: 196px; top: 10px;
    font-family: "Great Vibes", cursive; font-size: 76px; line-height: 1;
    color: #fff; text-shadow: 1px 1px 2px rgba(0,0,0,.45);
    transform: rotate(-4deg);
  }
  .subline {
    position: absolute; left: 200px; top: 150px; width: 320px; text-align: center;
    color: #1f2a2b; font-size: 24px; line-height: 1.2;
  }
  .invite {
    position: absolute; left: 0; top: 240px; width: 100%; text-align: center;
    font-family: "Dancing Script", cursive; font-weight: 600; font-size: 25px; line-height: 1.2;
    color: #111; font-style: italic;
  }
  .photo {
    position: absolute; border: 1px solid var(--teal);
  }
  .photo--ringcard {
    left: 29px; top: 319px; width: 277px; height: 413px;
    background: linear-gradient(160deg, #f4f4f6 0%, var(--photo-mid) 55%, #b7babf 100%);
  }
  .photo--tabledeco {
    left: 343px; top: 319px; width: 149px; height: 222px;
    background: linear-gradient(170deg, #9c9990 0%, #d8d6d2 50%, #bdbab3 100%);
  }
  .motto {
    position: absolute; left: 316px; top: 548px; width: 204px; text-align: center;
    font-size: 14.3px; line-height: 1.32;
  }
  .motto .closing { margin-top: 20px; }

  /* back */
  .assortment {
    position: absolute; left: 20px; top: 32px; width: 495px; text-align: center;
    font-size: 14.3px; line-height: 1.22;
  }
  .assortment p + p { margin-top: 16px; }
  .photo--favours {
    left: 36px; top: 306px; width: 460px; height: 309px;
    background: radial-gradient(ellipse at 45% 45%, #f6f6f8 0%, var(--photo-light) 45%, #b9bcc2 100%);
  }
  .page--back .shop-mark {
    left: 355px; top: 539px; width: 145px; height: 145px;
    background: var(--grey-mark); box-shadow: 0 2px 6px rgba(0,0,0,.35);
  }
  .footer-band {
    position: absolute; left: 0; bottom: 0; width: 100%; height: 106px;
    background: var(--teal);
    box-shadow: 0 -6px 8px -4px rgba(0,0,0,.3);
    color: #fff; font-size: 12.3px; line-height: 1.3;
  }
  .contact { position: absolute; left: 48px; top: 18px; }
  .hours { position: absolute; left: 276px; top: 18px; }
  .hours .gap { height: 16px; }
</style>
</head>
<body>
  <section class="page page--front">
    <header class="header-band">
      <div class="shop-mark"><span>Hartmann</span></div>
      <h1 class="headline">Do it yourself</h1>
      <p class="subline">Karten &amp; Hochzeitsdeko selbstgemacht</p>
    </header>
    <p class="invite">Wir würden uns freuen, Sie bei der Gestaltung Ihrer<br>ganz persönlichen Einladungskarte beraten zu dürfen!!!</p>
    <div class="photo photo--ringcard" role="img" aria-label="Foto: weiße Hochzeitskarte mit grünem Buchsbaumherz und Satinschleife"></div>
    <div class="photo photo--tabledeco" role="img" aria-label="Foto: Tischdekoration mit Karten, Herzen und Windlichtern"></div>
    <div class="motto">
      <p>Rege Hände geben<br>dem Körper Kraft,<br>dem Geist Bewegung<br>und der Seele Ruhe.<br>Tu, was du kannst, mit<br>dem was du hast,<br>dort, wo du bist!<br>Aus einfachen schöne<br>und edle Dinge machen –</p>
      <p class="closing">wir zeigen es Ihnen.</p>
    </div>
  </section>

  <section class="page page--back">
    <div class="assortment">
      <p>In unseren Räumen finden Sie Herziges und Glückbringendes,<br>Brautpaare, Tauben, Ringkissen,<br>Fotoalben, Gästebücher, Kerzen und Servietten.</p>
      <p>Eine Auswahl verschiedenster Papiere und Stempel,<br>zur Kartengestaltung für Hochzeit, Taufe, Konfirmation,<br>Geburtstag und sonstige Anlässe.<br>Wachsplatten und Stifte zum Kerzenverzieren.</p>
      <p>Verschiedene Variationen von Bändern, Kordeln<br>und Tüll für Kirchendekorationen und Autoschmuck.</p>
      <p>Glas- &nbsp;und Wachsperlen, Pailetten, Rocailles und Indianerperlen,<br>Straßsteine und Glaskristalle, Drähte, Verschlüsse und<br>Bänder zur Schmuckgestaltung.</p>
    </div>
    <div class="photo photo--favours" role="img" aria-label="Foto: weiße Gastgeschenk-Schachteln mit Aufschrift „wir heiraten“ und verstreutem Reis"></div>
    <div class="shop-mark"><span>Hartmann</span></div>
    <footer class="footer-band">
      <div class="contact">
        Hartmann Basteln und Dekorieren<br>
        Mühlenweg 14<br>
        21465 Lindenau<br>
        Tel.: 04152 - 47 12 30
      </div>
      <div class="hours">
        Öffnungszeiten:
        <div class="gap"></div>
        Montag-Samstag: 09.30-13.00 Uhr<br>
        Mo, Di, Do &amp; Fr: 14.30-18.00 Uhr
      </div>
    </footer>
  </section>
</body>
</html>
```